Business Card Design

We need a business card design for a new company based in Allen, Texas. (outside of Dallas,Texas) We offer Business Management Solutions to Entrepreneurs, as well as Corporate Businesses. Our product line offers solutions to Image, Branding, Social Media marketing, business development strategies, banking / funding solutions, just to name a few. We would like to see designs that convey strength and confidence. I have attached a sample design of our company name. Designers you may use company name as either: Vorlix or Vorlix Corporation, depending on the design layout.

Please show alternate color of Black as well.

Industry/Entity Type

Business

Contact Information for Business Card

Vorlix Corporation

2847 E. Hollowbrook Drive, STE 410
Larkmont, TX 75290
Office: 555.318.7742
Fax: 555.318.7743

Dr. Miles Dunworth
Business Development Director

```html
<!DOCTYPE html>
<html lang="en">
<head>
<meta charset="utf-8">
<title>Vorlix Corporation – Business Card</title>
<link rel="stylesheet" href="https://fonts.googleapis.com/css2?family=Fira+Sans:wght@300;400;600&display=swap">
<style>
  :root {
    --backdrop: #e6e6e6;
    --card-black: #1d1c1d;
    --brand-red: #d1373b;
    --accent-red: #c8282c;
    --ink-white: #ffffff;
    --ink-soft: #fbe3e3;
    --bar-black: #1a1a1a;
  }
  * { margin: 0; padding: 0; box-sizing: border-box; }
  html, body {
    width: 1200px; height: 1200px; overflow: hidden;
    background: var(--backdrop);
    font-family: "Fira Sans", Arial, sans-serif;
  }
  .canvas {
    position: relative; width: 1200px; height: 1200px;
    display: flex; flex-direction: column; align-items: center; justify-content: center; gap: 60px;
  }
  .card {
    position: relative; width: 700px; height: 400px; overflow: hidden;
    box-shadow: 0 6px 18px rgba(0,0,0,0.18);
  }

  /* Front */
  .card-front { background: var(--card-black); }
  .front-rule {
    position: absolute; left: 0; right: 0; top: 206px; height: 3px;
    background: var(--accent-red);
  }
  .front-wordmark {
    position: absolute; left: 50%; top: 150px; transform: translateX(-50%);
    padding: 0 26px; background: var(--card-black);
    color: var(--ink-white); font-weight: 400; font-size: 96px; line-height: 110px;
    letter-spacing: 2px;
  }

  /* Back */
  .card-back { background: var(--brand-red); color: var(--ink-white); }
  .edge-bar { position: absolute; width: 12px; background: var(--bar-black); }
  .edge-bar.left-top { left: 56px; top: 0; height: 90px; }
  .edge-bar.left-bottom { left: 56px; bottom: 0; height: 50px; }
  .edge-bar.right-top { right: 34px; top: 0; height: 60px; }
  .edge-bar.right-bottom { right: 34px; bottom: 0; height: 90px; }

  .back-logo {
    position: absolute; right: 90px; top: 96px; width: 170px; height: 82px;
    background: var(--bar-black);
    display: flex; align-items: center; justify-content: center;
    font-weight: 400; font-size: 40px; color: var(--ink-white); letter-spacing: 1px;
  }
  .contact { position: absolute; left: 96px; top: 90px; }
  .contact-name { font-weight: 600; font-size: 19px; }
  .contact-title { font-weight: 300; font-size: 15px; color: var(--ink-soft); margin-top: 2px; }
  .contact-address { font-weight: 300; font-size: 15px; margin-top: 22px; line-height: 20px; }
  .contact-lines { margin-top: 10px; list-style: none; }
  .contact-lines li {
    display: flex; align-items: center; gap: 10px;
    font-weight: 300; font-size: 15px; line-height: 24px;
  }
  .contact-lines svg { width: 14px; height: 14px; flex: none; }
</style>
</head>
<body>
<main class="canvas">
  <section class="card card-front" aria-label="Card front">
    <div class="front-rule"></div>
    <div class="front-wordmark">Vorlix</div>
  </section>

  <section class="card card-back" aria-label="Card back">
    <span class="edge-bar left-top"></span>
    <span class="edge-bar left-bottom"></span>
    <span class="edge-bar right-top"></span>
    <span class="edge-bar right-bottom"></span>

    <div class="contact">
      <p class="contact-name">Dr. Miles Dunworth</p>
      <p class="contact-title">Business Development Director</p>
      <p class="contact-address">Vorlix Corporation 2847 E. Hollowbrook Drive,<br>STE 410 Larkmont, TX 75290</p>
      <ul class="contact-lines">
        <li>
          <svg viewBox="0 0 14 14" aria-hidden="true"><rect width="14" height="14" fill="#1a1a1a"/><path d="M4 3h2l1 2-1 1a5 5 0 0 0 2 2l1-1 2 1v2c-4 0-7-3-7-7z" fill="#fff"/></svg>
          <span>555.318.7742</span>
        </li>
        <li>
          <svg viewBox="0 0 14 14" aria-hidden="true"><rect width="14" height="14" fill="#1a1a1a"/><rect x="3" y="6" width="8" height="5" fill="#fff"/><rect x="5" y="3" width="4" height="3" fill="#fff"/></svg>
          <span>555.318.7743</span>
        </li>
      </ul>
    </div>

    <div class="back-logo">Vorlix</div>
  </section>
</main>
</body>
</html>
```